Construction Company

Design a clutter free business card, it can be double-sided utilizing the logo for BDN Ltd simple with all relevant contact information.

Please also a letterhead design to function for the purposes of invoicing, all mail requirements, with header to be distinctive while the footer ties page together and incorporates all necessary information.

For now, please use generic / dummy text and when a winner is selected, I will disclose the contact information.

Hi Designers! Please read the updated brief which includes the design of a business card and letterhead. Thank you!

```html
<!DOCTYPE html>
<html lang="en">
<head>
<meta charset="utf-8">
<title>BDN Ltd – Business Card</title>
<link rel="stylesheet" href="https://fonts.googleapis.com/css2?family=Libre+Baskerville:wght@700&family=Arimo:wght@400;700&display=swap">
<style>
  :root {
    --stage: #2b2523;
    --card: #0b0b0b;
    --blue: #0a37a8;
    --gold: #c9a227;
    --text: #e6e6e6;
    --rule: #555;
  }
  html, body {
    margin: 0;
    width: 1200px;
    height: 842px;
    overflow: hidden;
    background: var(--stage);
  }
  .canvas {
    position: relative;
    width: 1200px;
    height: 842px;
  }
  .card {
    position: absolute;
    top: 272px;
    width: 520px;
    height: 297px;
    background: var(--card);
    box-shadow: 0 10px 30px rgba(0,0,0,.55);
    overflow: hidden;
  }
  .card--back { left: 50px; }
  .card--front { left: 630px; }

  /* contact side */
  .band {
    position: absolute;
    left: 0;
    width: 100%;
    height: 11px;
    background: var(--blue);
  }
  .band--top { top: 0; }
  .band--bottom { bottom: 0; }
  .details {
    position: absolute;
    left: 150px;
    top: 64px;
    font-family: "Arimo", Arial, sans-serif;
    color: var(--text);
  }
  .person-name {
    margin: 0;
    font-family: "Libre Baskerville", "Times New Roman", serif;
    font-weight: 700;
    font-size: 15px;
    letter-spacing: .5px;
    color: var(--gold);
  }
  .person-role {
    margin: 2px 0 0;
    font-size: 13px;
  }
  .rule {
    width: 190px;
    height: 1px;
    background: var(--rule);
    margin: 9px 0;
  }
  .contact {
    margin: 0;
    padding: 0;
    list-style: none;
    font-size: 13px;
    line-height: 17px;
  }
  .contact .label {
    color: var(--gold);
    font-weight: 700;
  }
  .contact .web { color: var(--gold); }
  .address {
    margin: 0;
    font-size: 13px;
    line-height: 17px;
  }

  /* brand side */
  .accent {
    position: absolute;
    width: 52px;
    height: 44px;
    background: var(--blue);
  }
  .accent::after {
    content: "";
    position: absolute;
    top: 0;
    width: 4px;
    height: 100%;
    background: var(--gold);
  }
  .accent--top { top: 44px; right: 0; }
  .accent--top::after { left: 0; }
  .accent--side { top: 185px; left: 0; }
  .accent--side::after { right: 0; }
  .brand {
    position: absolute;
    inset: 0;
    display: flex;
    align-items: center;
    justify-content: center;
  }
  .brand-name {
    font-family: "Arimo", Arial, sans-serif;
    font-weight: 700;
    font-size: 30px;
    letter-spacing: 1px;
    color: var(--text);
  }
</style>
</head>
<body>
<main class="canvas">
  <section class="card card--back" aria-label="Business card, contact side">
    <div class="band band--top"></div>
    <div class="details">
      <h1 class="person-name">DANIEL HARTLEY</h1>
      <p class="person-role">Managing Director</p>
      <div class="rule"></div>
      <ul class="contact">
        <li><span class="label">P:</span> 044-555 010 234</li>
        <li><span class="label">M:</span> 044-555 010 234</li>
        <li><span class="label">E:</span> info@example.com</li>
        <li class="web">www.example.com</li>
      </ul>
      <div class="rule"></div>
      <p class="address">12345, Address Goes Here<br>Country Name, 123456</p>
    </div>
    <div class="band band--bottom"></div>
  </section>

  <section class="card card--front" aria-label="Business card, brand side">
    <div class="accent accent--top"></div>
    <div class="accent accent--side"></div>
    <div class="brand">
      <span class="brand-name">BDN Ltd</span>
    </div>
  </section>
</main>
</body>
</html>
```